Keeep it up is our company motto. Need "keeep it up" sticker design for promotional pur...

I need a sticker design for my upstart company called Plumvex which I like to describe as The Friendly Tovari Pal of Personal Growth. I'm looking for a cleanly designed combination mark that joins together our logo (see uploaded file) and the phrase "keeep it up." The 3 E's stand for Everyday Earnest Effort. One or two colors maximum. The phrase may be split up vertically or horizontally and the logo may also be tweaked a bit if needed. Overall design should be simple and easily recognizable.

```html
<!DOCTYPE html>
<html lang="en">
<head>
<meta charset="utf-8">
<title>Keeep It Up Sticker</title>
<link rel="stylesheet" href="https://fonts.googleapis.com/css2?family=Archivo+Black&display=swap">
<style>
  :root {
    --backdrop: #2a2a2a;
    --sticker-yellow: #fff200;
    --frame-black: #000000;
    --ink-black: #141414;
  }
  html, body {
    margin: 0;
    padding: 0;
    width: 1200px;
    height: 997px;
    overflow: hidden;
    background: var(--backdrop);
  }
  .canvas {
    position: relative;
    width: 1200px;
    height: 997px;
  }
  .sticker {
    position: absolute;
    left: 260px;
    top: 256px;
    width: 680px;
    height: 459px;
  }
  .sticker text {
    font-family: "Archivo Black", "Arial Black", sans-serif;
    fill: var(--ink-black);
  }
</style>
</head>
<body>
<main class="canvas">
  <svg class="sticker" viewBox="0 0 680 459" xmlns="http://www.w3.org/2000/svg" aria-label="Keeep it up sticker by Plumvex">
    <rect class="sticker-edge" x="0" y="0" width="680" height="459" fill="var(--sticker-yellow)"/>
    <rect class="sticker-frame" x="5" y="5" width="670" height="449" fill="var(--frame-black)"/>
    <rect class="sticker-panel" x="39" y="31" width="606" height="393" fill="var(--sticker-yellow)"/>

    <circle class="brand-dot" cx="222" cy="104" r="10" fill="var(--ink-black)"/>
    <text class="brand-name" x="244" y="120" font-size="44" textLength="200" lengthAdjust="spacingAndGlyphs">Plumvex</text>

    <text class="motto-line-one" x="75" y="284" font-size="180" textLength="560" lengthAdjust="spacingAndGlyphs">KEEEP</text>
    <text class="motto-line-two" x="200" y="404" font-size="132" textLength="300" lengthAdjust="spacingAndGlyphs">IT UP</text>
  </svg>
</main>
</body>
</html>
```